(4) Bowling League Designs 1920x1080

Will be used on our website and in some digital signage.

We are starting (4) leagues this summer and need a basic graphic as an attention grab which will then lead the customer to full information / sign ups. The information I would need on each one is as follows:

1. Monday Night FREE ball league - Begins May 3rd

2. Tuesday Trios - KFDL Sanctioned - Begins May 11th
$9,000 prize fund

3. Wednesday Cosmic League - 9 pin no tap fun league - May 12th start

4. Thursday Night FREE ball league - Begins May 13th

I will attach some random examples of previous ones to give you an idea.

```html
<!DOCTYPE html>
<html lang="en">
<head>
<meta charset="utf-8">
<title>Summer Bowling Leagues</title>
<link rel="stylesheet" href="https://fonts.googleapis.com/css2?family=Roboto+Condensed:wght@400;700;800&display=swap">
<style>
  :root {
    --page: #ffffff;
    --panel: #1b1b1b;
    --band: #050505;
    --gold: #f2a91c;
    --white: #ffffff;
    --red: #e3202a;
    --ink: #000000;
  }
  html, body {
    margin: 0;
    padding: 0;
    width: 1200px;
    height: 960px;
    overflow: hidden;
    background: var(--page);
  }
  .league-board {
    display: block;
    width: 1200px;
    height: 960px;
    font-family: "Roboto Condensed", "Arial Narrow", sans-serif;
  }
  .day-label { fill: var(--white); font-weight: 400; font-size: 40px; }
  .league-title { fill: var(--white); font-weight: 800; font-size: 68px; letter-spacing: 1px; }
  .start-date { fill: var(--white); font-weight: 700; font-size: 30px; }
  .prize { fill: var(--red); font-weight: 800; font-size: 62px; }
  .outlined { stroke: var(--ink); stroke-width: 4px; paint-order: stroke fill; }
  .band { fill: var(--band); }
  .band-rule { fill: var(--gold); }
</style>
</head>
<body>
<svg class="league-board" viewBox="0 0 1500 1200" xmlns="http://www.w3.org/2000/svg">
  <defs>
    <linearGradient id="panel-shade" x1="0" y1="0" x2="0" y2="1">
      <stop offset="0" stop-color="#2a2a2a"/>
      <stop offset="0.5" stop-color="#1a1a1a"/>
      <stop offset="1" stop-color="#141414"/>
    </linearGradient>
    <linearGradient id="flame-streak" x1="0" y1="0" x2="1" y2="0">
      <stop offset="0" stop-color="#f08a4a" stop-opacity="0.2"/>
      <stop offset="0.4" stop-color="#f7a060" stop-opacity="0.85"/>
      <stop offset="1" stop-color="#e5602a" stop-opacity="0.6"/>
    </linearGradient>
    <radialGradient id="ball-glow" cx="0.4" cy="0.5" r="0.6">
      <stop offset="0" stop-color="#f7b060"/>
      <stop offset="0.6" stop-color="#d8561f"/>
      <stop offset="1" stop-color="#1b1b1b" stop-opacity="0"/>
    </radialGradient>
    <linearGradient id="pins-tone" x1="0" y1="0" x2="1" y2="1">
      <stop offset="0" stop-color="#f4f4f4"/>
      <stop offset="1" stop-color="#b9b9b9"/>
    </linearGradient>
  </defs>

  <!-- panel -->
  <rect x="72" y="218" width="1356" height="763" fill="url(#panel-shade)"/>

  <!-- decorative artwork areas -->
  <rect x="72" y="770" width="820" height="190" fill="url(#flame-streak)" role="img" aria-label="Fiery motion streak behind a rolling bowling ball"/>
  <rect x="1100" y="660" width="328" height="321" fill="url(#ball-glow)" role="img" aria-label="Orange bowling ball wrapped in flames"/>
  <rect x="1035" y="218" width="370" height="320" rx="30" fill="url(#pins-tone)" opacity="0.9" role="img" aria-label="Two white bowling pins with red stripes"/>

  <!-- Tuesday band -->
  <polygon class="band-rule" points="72,560 1030,285 1030,298 72,573"/>
  <polygon class="band" points="72,585 1030,293 1030,478 72,770"/>
  <polygon class="band-rule" points="72,765 1030,473 1030,484 72,776"/>

  <!-- Wednesday band -->
  <polygon class="band-rule" points="470,690 1428,428 1428,440 470,702"/>
  <polygon class="band" points="470,700 1428,438 1428,635 470,897"/>
  <polygon class="band-rule" points="470,892 1428,628 1428,640 470,904"/>

  <!-- Monday -->
  <g class="league monday">
    <text class="day-label" x="110" y="302">MONDAY NIGHT</text>
    <text class="league-title" x="108" y="380">FREE BALL LEAGUE</text>
    <text class="start-date" x="110" y="425">Begins May 3rd</text>
  </g>

  <!-- Tuesday -->
  <g class="league tuesday" transform="rotate(-16.5 160 690)">
    <text class="day-label" x="140" y="620">TUESDAY TRIOS</text>
    <text class="league-title" x="150" y="690">KFDL SANCTIONED</text>
    <text class="prize" x="520" y="612">$9,000 prize fund</text>
    <text class="start-date" x="715" y="672">Begins May 11th</text>
  </g>

  <!-- Wednesday -->
  <g class="league wednesday" transform="rotate(-16.5 520 850)">
    <text class="day-label" x="505" y="770">WEDNESDAY COSMIC LEAGUE</text>
    <text class="league-title" x="515" y="850" style="font-size:72px">9 PIN NO TAP FUN LEAGUE</text>
    <text class="start-date" x="1130" y="770">May 12th start</text>
  </g>

  <!-- Thursday -->
  <g class="league thursday" text-anchor="end">
    <text class="day-label outlined" x="1392" y="818">THURSDAY NIGHT</text>
    <text class="league-title outlined" x="1392" y="893">FREE BALL LEAGUE</text>
    <text class="start-date outlined" x="1392" y="937">Begins May 13th</text>
  </g>
</svg>
</body>
</html>
```